2013 Golf Outing Flyer

Our charitable organization was created in honor of my daughter who died at age 16. Our annual fundraiser is a golf tournament. I am not a creative person so I'd like someone to design a printable flyer that grabs people's attention but is not too busy while incorportating our organization's logo with the basic information.

Event details:
3rd Annual Marissa Joan Caldwell Memorial Golf Tournament
4 person scramble

Saturday October 5th, 2013
Larkspur Golf Club, Auburn, IL
9:30 Registration
Shotgun start at noon
To Register go online to www.marissajcaldwellgolf.teesignups.example or email
marissacaldwellfund@mailbox.example

Scholarships to Cedar Rapids Hollow High School seniors are made possible by our orgnization through this fundraiser.
Updates

Target Market(s)

golfers and businesses willing to sponsor event

Industry/Entity Type

School

Requirements
Must have
• single page-easy to print
includes non profit organization logo which I attached (think I did)
Specific information about the tournament- date and location and registration info
Nice to have
• company logo and the golf outing logo but if both are too much, then just the golf logo and the organization name can be at the bottom

```html
<!DOCTYPE html>
<html lang="en">
<head>
<meta charset="utf-8">
<title>Marissa Joan Caldwell Memorial Golf Tournament Flyer</title>
<link rel="stylesheet" href="https://fonts.googleapis.com/css2?family=Didact+Gothic&family=Marcellus&display=swap">
<style>
  :root {
    --page: #ffffff;
    --frame: #5a3d20;
    --paper: #f4efe1;
    --paper-edge: #d9d1bc;
    --paper-shadow: #6d6456;
    --grass-light: #7fbf3a;
    --grass-mid: #4f9a24;
    --grass-dark: #2d6414;
    --title: #a6a23a;
    --detail: #3b2a18;
    --register: #ada94e;
    --rule: #8a7d62;
  }
  * { margin: 0; padding: 0; box-sizing: border-box; }
  html, body {
    width: 1200px; height: 1200px; overflow: hidden;
    background: var(--page);
  }
  .flyer {
    position: absolute;
    left: 40px; top: 337px;
    width: 1120px; height: 526px;
    background: var(--frame);
  }
  .flyer__field {
    position: absolute;
    left: 26px; top: 26px; right: 26px; bottom: 26px;
    overflow: hidden;
    background:
      radial-gradient(ellipse 42% 60% at 57% 48%, var(--paper) 55%, var(--paper-edge) 85%, var(--paper-shadow) 120%);
  }
  .flyer__grass {
    position: absolute; top: 0; height: 100%;
  }
  .flyer__grass--left { left: 0; width: 330px; }
  .flyer__grass--right { right: 0; width: 200px; }
  .flyer__content {
    position: absolute;
    left: 0; top: 0; width: 100%; height: 100%;
    text-align: center;
  }
  .event-mark {
    position: absolute; left: 631px; transform: translateX(-50%);
    top: 34px;
    font-family: "Didact Gothic", sans-serif;
    color: var(--grass-mid);
    white-space: nowrap;
  }
  .event-mark__initials { display: block; font-size: 46px; line-height: 1; letter-spacing: 4px; }
  .event-mark__tagline { display: block; font-size: 18px; margin-top: 6px; }
  .event-title {
    position: absolute; left: 631px; transform: translateX(-50%);
    top: 142px;
    font-family: "Didact Gothic", sans-serif;
    font-weight: 400;
    font-size: 34px; line-height: 41px;
    color: var(--title);
    white-space: nowrap;
  }
  .event-format {
    position: absolute; left: 631px; transform: translateX(-50%);
    top: 238px;
    font-family: "Marcellus", serif;
    font-size: 23px; letter-spacing: 1px;
    color: var(--detail);
    white-space: nowrap;
  }
  .event-details {
    position: absolute; left: 631px; transform: translateX(-50%);
    top: 279px;
    list-style: none;
    font-family: "Marcellus", serif;
    font-size: 18px; line-height: 24.5px;
    color: var(--detail);
    text-transform: uppercase;
    white-space: nowrap;
  }
  .event-rule {
    position: absolute; left: 379px; top: 390px;
    width: 514px; height: 0;
    border-top: 1px dotted var(--rule);
  }
  .event-register {
    position: absolute; left: 631px; transform: translateX(-50%);
    top: 407px;
    font-family: "Didact Gothic", sans-serif;
    font-size: 16px; line-height: 25px;
    color: var(--register);
    white-space: nowrap;
  }
</style>
</head>
<body>
  <main class="flyer">
    <div class="flyer__field">
      <svg class="flyer__grass flyer__grass--left" viewBox="0 0 330 474" preserveAspectRatio="none" role="img" aria-label="Close-up photograph of green putting-green grass with a white golf ball resting near the bottom">
        <defs>
          <linearGradient id="grassLeft" x1="0" y1="0" x2="1" y2="0">
            <stop offset="0" stop-color="var(--grass-dark)"/>
            <stop offset="0.55" stop-color="var(--grass-mid)"/>
            <stop offset="1" stop-color="var(--grass-light)"/>
          </linearGradient>
        </defs>
        <path d="M0 0 H300 C280 60 250 110 220 170 C190 240 175 300 185 380 C190 420 205 450 215 474 H0 Z" fill="url(#grassLeft)"/>
      </svg>
      <svg class="flyer__grass flyer__grass--right" viewBox="0 0 200 474" preserveAspectRatio="none" role="img" aria-label="Close-up photograph of green grass along the right edge">
        <defs>
          <linearGradient id="grassRight" x1="1" y1="0" x2="0" y2="0">
            <stop offset="0" stop-color="var(--grass-dark)"/>
            <stop offset="0.6" stop-color="var(--grass-mid)"/>
            <stop offset="1" stop-color="var(--grass-light)"/>
          </linearGradient>
        </defs>
        <path d="M200 0 H20 C50 70 80 150 85 230 C90 320 60 400 40 474 H200 Z" fill="url(#grassRight)"/>
      </svg>

      <div class="flyer__content">
        <div class="event-mark">
          <span class="event-mark__initials">MJC</span>
          <span class="event-mark__tagline">Memorial Golf Outing</span>
        </div>
        <h1 class="event-title">3rd Annual Marissa Joan Caldwell<br>Memorial Golf Tournament</h1>
        <h2 class="event-format">4 PERSON SCRAMBLE</h2>
        <ul class="event-details">
          <li>Saturday October 5th, 2013</li>
          <li>Larkspur Golf Club, Auburn, IL</li>
          <li>9:30 Registration</li>
          <li>Shotgun Start at Noon</li>
        </ul>
        <div class="event-rule"></div>
        <p class="event-register">To register go online: www.marissajcaldwellgolf.teesignups.example<br>or email: marissacaldwellfund@mailbox.example</p>
      </div>
    </div>
  </main>
</body>
</html>
```